Multivitamin fruit drink in tetrapak

Label design for a 200 ml tetrapak which contains fruit juice with multivitamins in natural form . Product will be promoted to doctors and will follow a otx model. The target is children and women. Being a completely natural fortified multivitamin and mineral drink , the natural aspects to be highlighted. A white background is suggestive . Should not have more than 6 colors as this involves flexo printing.

Target Market(s)

Children and women through doctors recommendations

Industry/Entity Type

Pharmaceutical

Font styles to use
Serif
Sans Serif
Decorative

Requirements
Must have
• Pictures of fruit . Variant 1 is mango and variant 2 is orange. Brand name is Verosta. Can also suggest new names.
Nice to have
• The brand standing out, with white or softer color background
Should not have
• Should not have Dark background. Not funky or too colorful.

```html
<!DOCTYPE html>
<html lang="en">
<head>
<meta charset="utf-8">
<title>Verosta Mango – 200 ml Carton Front Panel</title>
<link rel="stylesheet" href="https://fonts.googleapis.com/css2?family=Fredoka:wght@400;500;600;700&display=swap">
<style>
  :root {
    --mango-orange: #f2a22a;
    --mango-deep: #e08a12;
    --drop-light: #f8c456;
    --leaf-green: #2f9a3a;
    --ink: #3a3a3a;
    --paper: #ffffff;
    --fruit-yellow: #f6c43a;
    --fruit-shade: #e3a21c;
  }
  * { margin: 0; padding: 0; box-sizing: border-box; }
  html, body {
    width: 849px;
    height: 1200px;
    overflow: hidden;
    background: var(--paper);
  }
  .carton-front {
    position: relative;
    width: 849px;
    height: 1200px;
    background: var(--paper);
    font-family: "Fredoka", sans-serif;
    color: var(--ink);
  }
  .top-band {
    position: absolute;
    top: 0;
    left: 0;
    width: 849px;
    height: 220px;
    background: var(--mango-orange);
  }
  .brand-name {
    position: absolute;
    top: 68px;
    width: 100%;
    text-align: center;
    font-size: 92px;
    font-weight: 600;
    line-height: 1;
    color: var(--paper);
    letter-spacing: 1px;
  }
  .juice-drop-visual {
    position: absolute;
    top: 220px;
    left: 345px;
    width: 160px;
    height: 360px;
    border-radius: 0 0 80px 80px;
    background: linear-gradient(180deg, var(--mango-orange) 0%, var(--drop-light) 65%, var(--mango-deep) 100%);
  }
  .product-name {
    position: absolute;
    top: 600px;
    width: 100%;
    text-align: center;
    font-size: 150px;
    font-weight: 700;
    color: var(--mango-orange);
    line-height: 1;
    letter-spacing: 2px;
  }
  .claim {
    position: absolute;
    top: 752px;
    width: 100%;
    text-align: center;
    font-size: 44px;
    font-weight: 600;
    line-height: 1;
    color: var(--leaf-green);
  }
  .fortified-note {
    position: absolute;
    top: 815px;
    left: 340px;
    width: 420px;
    font-size: 34px;
    font-weight: 500;
    line-height: 1.15;
    color: var(--ink);
  }
  .fruit-visual {
    position: absolute;
    top: 925px;
    left: 200px;
    width: 400px;
    height: 185px;
    border-radius: 50%;
    background: radial-gradient(ellipse at 40% 35%, var(--fruit-yellow) 0%, var(--fruit-shade) 100%);
  }
  .net-volume {
    position: absolute;
    bottom: 38px;
    right: 60px;
    font-size: 38px;
    font-weight: 500;
    line-height: 1;
    color: var(--ink);
  }
</style>
</head>
<body>
<main class="carton-front">
  <div class="top-band"></div>
  <div class="brand-name">Verosta</div>

  <div class="juice-drop-visual" role="img" aria-label="Illustration of mango juice dripping into a single glossy drop"></div>

  <h1 class="product-name">MANGO</h1>
  <p class="claim">100% fruit Juice</p>
  <p class="fortified-note">fortified with natural vitamins and minerals</p>

  <div class="fruit-visual" role="img" aria-label="Photo of a ripe yellow mango"></div>

  <p class="net-volume">Net wt:200ml</p>
</main>
</body>
</html>
```